Local Finance and Insurance Advising Company from Switzerland needs an impressive banner design.

I am looking for an impressive Banner Design, I need this Banner for Facebook, LinkedIn, YouTube & Google.

I am Advising all kind of peoples who are living here in Switzerland. Young, middle age and old people. People who want to go study, people who are planning to create a family, old people who are, or going to retire. Expatriates who want to leave Switzerland to live in another country, expatriates who are coming to Switzerland. Peoples who ant to build their own business up. All kind of financial, insurance and pension planning's.

The Company Name is: Alpine Counsel
Our slogen / heading is: Clear Guidance, no Pitch

The Company logo can be used for the banner, but I would preffer to have the banner without logo, as the logo will be already in a another field on the social networks.

Since the first impression is the most important, this project is really important to me. I am ready to realize further projects with the one who can create the perfect banner who hits the point as described. I am a start-up company, everything is still on beginning and still much has to be done.

Target Market(s)

private clients

Requirements
Must have
• The banner should give the impression of happiness, safeness, health and freedom. Empowering people and creating freedom lifestyles.
Should not have
• I do not want that the banner looks like we are some kind of broker who is just selling some kind of insurances.

```html
<!DOCTYPE html>
<html lang="en">
<head>
<meta charset="utf-8">
<title>Alpine Counsel – Clear Guidance, no Pitch</title>
<link rel="stylesheet" href="https://fonts.googleapis.com/css2?family=Montserrat:wght@400;600;800&display=swap">
<style>
  :root {
    --brand-red: #e3101a;
    --brand-red-soft: #f28a8f;
    --paper: #ffffff;
    --sky-top: #a9cbe8;
    --sky-mid: #c9dcea;
    --scene-warm: #c7b9a4;
    --scene-green: #7f8c5e;
  }
  * { margin: 0; padding: 0; box-sizing: border-box; }
  html, body {
    width: 1200px;
    height: 671px;
    overflow: hidden;
    background: var(--paper);
  }
  .banner {
    position: relative;
    width: 1200px;
    height: 671px;
    overflow: hidden;
    font-family: "Montserrat", sans-serif;
  }
  .banner__photo {
    position: absolute;
    inset: 0;
    background:
      linear-gradient(180deg, var(--sky-top) 0%, var(--sky-mid) 58%, var(--scene-green) 78%, var(--scene-warm) 100%);
  }
  .banner__shapes {
    position: absolute;
    inset: 0;
    width: 1200px;
    height: 671px;
  }
  .shape--accent { fill: var(--brand-red-soft); }
  .shape--red { fill: var(--brand-red); }
  .shape--white { fill: var(--paper); }

  .headline {
    position: absolute;
    left: 80px;
    top: 118px;
    color: var(--paper);
    text-transform: uppercase;
    font-size: 60px;
    line-height: 84px;
    letter-spacing: 0.5px;
  }
  .headline__strong { display: block; font-weight: 800; }
  .headline__light { display: block; font-weight: 400; }

  .brand-name {
    position: absolute;
    left: 102px;
    top: 606px;
    color: var(--brand-red);
    font-weight: 600;
    font-size: 26px;
    letter-spacing: 0.5px;
  }
</style>
</head>
<body>
  <main class="banner">
    <div class="banner__photo" role="img" aria-label="Photo of a smiling retired couple in sun hats taking a selfie outdoors on a hilltop, arms raised under a clear blue sky with a river landscape behind"></div>

    <svg class="banner__shapes" viewBox="0 0 1200 671" preserveAspectRatio="none" aria-hidden="true">
      <path class="shape--accent" d="M0,0 H872 C770,20 712,190 672,350 C640,470 590,540 480,566 L0,600 Z"/>
      <path class="shape--red" d="M0,0 H830 C722,22 678,182 640,340 C612,452 562,522 452,560 C352,588 252,540 152,560 C82,575 22,640 0,671 Z"/>
      <path class="shape--white" d="M0,671 C30,600 110,548 220,545 C330,542 420,578 520,566 C590,556 640,520 690,462 C668,560 610,640 572,671 Z"/>
      <path class="shape--white" d="M560,671 C620,640 660,602 725,600 C805,598 855,648 965,671 Z"/>
      <path class="shape--white" d="M1080,671 C1140,660 1182,620 1200,520 V671 Z"/>
    </svg>

    <h1 class="headline">
      <span class="headline__strong">Clear</span>
      <span class="headline__strong">Guidance,</span>
      <span class="headline__light">No Pitch</span>
    </h1>

    <div class="brand-name">Alpine Counsel</div>
  </main>
</body>
</html>
```